Steelcrest Process Systems. Needs a Business Card Design

We need a business card design for an engineering company which supplies industrial components (pumps, compressors, mechanical seals) provides repairs and services for above mentioned equipments. We offer a uniqe engineering solutions which help our customers to increase the productivness of their manufacturings, and energy savings.

Target Market(s)

Chemical and energy plants, refineries. Food industry and private consumers in a less.

Industry/Entity Type

Business

Contact Information for Business Card

Stylish and sleek design oriented on industrial area.

Requirements
Should not have
• company name shortening

```html
<!DOCTYPE html>
<html lang="en">
<head>
<meta charset="utf-8">
<title>Steelcrest Process Systems – Business Card</title>
<link href="https://fonts.googleapis.com/css2?family=Open+Sans:wght@400;600&display=swap" rel="stylesheet">
<style>
  :root {
    --backdrop: #e9e6e1;
    --card: #fbfbfb;
    --brand-blue: #2e3f9e;
    --brand-orange: #e5a12a;
    --brand-red: #d93b35;
    --contact-green: #3d8a3a;
    --ink: #4a4a4a;
    --divider: #cfcfcf;
  }
  * { box-sizing: border-box; margin: 0; padding: 0; }
  html, body {
    width: 1200px;
    height: 738px;
    overflow: hidden;
    background: var(--backdrop);
    font-family: "Open Sans", sans-serif;
  }
  .stage {
    position: relative;
    width: 1200px;
    height: 738px;
    display: flex;
    align-items: center;
    justify-content: center;
    gap: 60px;
  }
  .card {
    position: relative;
    width: 520px;
    height: 300px;
    background: var(--card);
    box-shadow: 0 6px 18px rgba(0, 0, 0, 0.12);
    overflow: hidden;
  }
  .brand {
    display: flex;
    flex-direction: column;
    align-items: center;
    gap: 14px;
  }
  .brand-mark {
    width: 44px;
    height: 44px;
    border-radius: 50%;
    background: var(--brand-blue);
  }
  .brand-name {
    font-weight: 600;
    color: var(--brand-blue);
    white-space: nowrap;
  }
  .card-front {
    display: flex;
    align-items: center;
    justify-content: center;
  }
  .card-front .brand-name { font-size: 26px; }
  .card-back .brand {
    position: absolute;
    left: 0;
    top: 62px;
    width: 300px;
  }
  .card-back .brand-mark { width: 38px; height: 38px; }
  .card-back .brand-name { font-size: 18px; }
  .divider {
    position: absolute;
    left: 300px;
    top: 36px;
    width: 1px;
    height: 200px;
    background: var(--divider);
  }
  .contact {
    position: absolute;
    left: 318px;
    top: 36px;
    color: var(--ink);
    font-size: 11.5px;
    line-height: 1.5;
  }
  .contact-name {
    font-size: 16px;
    font-weight: 600;
    color: var(--brand-blue);
    line-height: 1.2;
  }
  .contact-title {
    font-size: 13px;
    font-weight: 600;
    color: var(--brand-red);
    margin-bottom: 12px;
  }
  .contact-address { margin-bottom: 10px; }
  .label-phone { color: var(--brand-blue); }
  .label-fax { color: var(--contact-green); }
  .stripe {
    position: absolute;
    left: 0;
    bottom: 0;
    width: 520px;
    height: 12px;
    display: block;
  }
</style>
</head>
<body>
<main class="stage">
  <section class="card card-front" aria-label="Business card front">
    <div class="brand">
      <span class="brand-mark"></span>
      <span class="brand-name">Steelcrest Process Systems</span>
    </div>
  </section>

  <section class="card card-back" aria-label="Business card back">
    <div class="brand">
      <span class="brand-mark"></span>
      <span class="brand-name">Steelcrest Process Systems</span>
    </div>
    <div class="divider"></div>
    <div class="contact">
      <p class="contact-name">First &amp; Lastname</p>
      <p class="contact-title">Job Title</p>
      <p class="contact-address">123 Some place, in some<br>City, Some Country Code</p>
      <p><span class="label-phone">P.</span>500-000-1230</p>
      <p><span class="label-fax">F.</span>500-000-1230</p>
      <p>info@steelcrestprocess.com</p>
      <p>www.steelcrestprocess.com</p>
    </div>
    <svg class="stripe" viewBox="0 0 520 12" aria-hidden="true">
      <polygon points="0,0 212,0 200,12 0,12" fill="var(--brand-blue)"/>
      <polygon points="216,0 448,0 436,12 204,12" fill="var(--brand-orange)"/>
      <polygon points="452,0 520,0 520,12 440,12" fill="var(--brand-red)"/>
    </svg>
  </section>
</main>
</body>
</html>
```